Business card design needed

We need a new business card design to re launch my carpentry business. Could include double sided card with list of services provided.
Kitchens, bathrooms, decks, pergolas, window replacements, timber floor installation, owner builder assistance and general carpentry.
Would like an eye catching card that becons to be read in bright colors that has a logo that could be also used on clothing vehicle sinage etc
Preferably in blues and reds we live near beach so maybe some type of Beecher feel
Target Market(s)
The target market of my business would be mainly individuals requiring professional carpentry services not just a handy man. The renovation market plays a big part of my business
Industry/Entity Type
Carpentry
Contact Information for Business Card
Carpenter & joiner
Rob Pelham
Inverloch
gilda_robbo@tarnmail.com
0439862150
Look and feel
Each slider illustrates characteristics of the customer's brand and the style your logo design should communicate.

```html
<!DOCTYPE html>
<html lang="en">
<head>
<meta charset="utf-8">
<title>Services – Carpentry Business Card</title>
<link rel="stylesheet" href="https://fonts.googleapis.com/css2?family=Open+Sans:wght@400;600&display=swap">
<style>
  :root {
    --band-light: #c9614f;
    --band-mid: #b8493d;
    --band-deep: #8e1a1c;
    --panel-dark: #3a0707;
    --panel-mid: #6e1e1a;
    --panel-right: #8a3a30;
    --panel-right-light: #a8524a;
    --seam: #c46a5c;
    --emboss-ink: #8c2a26;
    --emboss-shade: rgba(40, 0, 0, 0.85);
    --emboss-light: rgba(255, 170, 150, 0.35);
  }
  html, body {
    margin: 0;
    padding: 0;
    width: 1200px;
    height: 741px;
    overflow: hidden;
    background: var(--seam);
  }
  .card {
    position: relative;
    width: 1200px;
    height: 741px;
    overflow: hidden;
    background: var(--seam);
    font-family: "Open Sans", "Calibri", sans-serif;
  }
  .card-shapes {
    position: absolute;
    inset: 0;
  }
  .heading {
    position: absolute;
    left: 81px;
    top: 202px;
    margin: 0;
    font-size: 47px;
    font-weight: 600;
    line-height: 1;
    letter-spacing: -0.5px;
    color: var(--emboss-ink);
    text-shadow: -1px -1px 1px var(--emboss-shade), 1px 1px 1px var(--emboss-light);
  }
  .service-list {
    position: absolute;
    right: 92px;
    top: 343px;
    margin: 0;
    padding: 0;
    list-style: none;
    text-align: right;
    font-size: 39px;
    line-height: 40.5px;
    letter-spacing: -0.5px;
    color: var(--emboss-ink);
    text-shadow: -1px -1px 1px var(--emboss-shade), 1px 1px 1px var(--emboss-light);
  }
</style>
</head>
<body>
<main class="card">
  <svg class="card-shapes" width="1200" height="741" viewBox="0 0 1200 741" aria-hidden="true">
    <defs>
      <linearGradient id="band-fill" x1="0" y1="0" x2="1" y2="0">
        <stop offset="0" stop-color="var(--band-light)"/>
        <stop offset="0.55" stop-color="var(--band-mid)"/>
        <stop offset="1" stop-color="var(--band-deep)"/>
      </linearGradient>
      <radialGradient id="band-glow" cx="0.72" cy="0" r="0.45">
        <stop offset="0" stop-color="#a50f12" stop-opacity="0.7"/>
        <stop offset="1" stop-color="#a50f12" stop-opacity="0"/>
      </radialGradient>
      <radialGradient id="left-panel-fill" cx="0.55" cy="0.45" r="0.7">
        <stop offset="0" stop-color="var(--panel-mid)"/>
        <stop offset="1" stop-color="var(--panel-dark)"/>
      </radialGradient>
      <radialGradient id="right-panel-fill" cx="0.45" cy="0.6" r="0.75">
        <stop offset="0" stop-color="var(--panel-right-light)"/>
        <stop offset="1" stop-color="#6a1f1a"/>
      </radialGradient>
    </defs>
    <rect class="top-band" x="0" y="0" width="1200" height="283" fill="url(#band-fill)"/>
    <rect class="top-band-glow" x="0" y="0" width="1200" height="283" fill="url(#band-glow)"/>
    <polygon class="panel-left" points="0,283 638,283 481,741 0,741" fill="url(#left-panel-fill)"/>
    <polygon class="panel-right" points="657,283 1200,283 1200,741 499,741" fill="url(#right-panel-fill)"/>
  </svg>

  <h1 class="heading">Services</h1>

  <ul class="service-list">
    <li>Kitchens</li>
    <li>Bathrooms</li>
    <li>Decks</li>
    <li>Pergolas</li>
    <li>Window replacements</li>
    <li>Tmber floor installation</li>
    <li>Owner builder assistance</li>
    <li>&amp; General carpentry</li>
  </ul>
</main>
</body>
</html>
```